Book Cover "Venice"

Creation of a cover (14 x 20.5 cm + bleed area) for a book:
Image: “BrumeVerte” (Tiff joined)
AUTHOR: Corinne Valmer
TITLE: The murmurs of Lorient
PUBLISHER: Editions Pluvane (AT THE BOTTOM OF THE COVER)

Target Market(s)

Readers of romantic novels

Industry/Entity Type

Book

```html
<!DOCTYPE html>
<html lang="fr">
<head>
<meta charset="utf-8">
<title>Les Murmures de Lorient — Corinne Valmer</title>
<link rel="stylesheet" href="https://fonts.googleapis.com/css2?family=Cinzel:wght@600;700&display=swap">
<style>
  :root {
    --page-bg: #ffffff;
    --cover-black: #12100e;
    --accent-red: #e0241a;
    --sky-red: #e2381e;
    --sky-deep: #9e1a10;
    --type-white: #ffffff;
  }
  html, body {
    margin: 0;
    width: 1200px;
    height: 1200px;
    overflow: hidden;
    background: var(--page-bg);
  }
  .cover {
    position: absolute;
    left: 319px;
    top: 178px;
    width: 563px;
    height: 843px;
    background: var(--cover-black);
    overflow: hidden;
    font-family: "Cinzel", serif;
    color: var(--type-white);
  }
  .cover-photo {
    position: absolute;
    left: 0; top: 0;
    width: 100%;
    height: 445px;
    background:
      linear-gradient(180deg, rgba(18,16,14,0) 45%, rgba(18,16,14,0.85) 80%, var(--cover-black) 100%),
      radial-gradient(ellipse at 60% 30%, var(--sky-red) 0%, var(--sky-deep) 75%);
  }
  .author {
    position: absolute;
    top: 16px;
    left: 0; right: 0;
    text-align: center;
    font-size: 29px;
    font-weight: 700;
    letter-spacing: 0.5px;
  }
  .title {
    position: absolute;
    left: 0; right: 0;
    margin: 0;
    font-weight: 700;
  }
  .title-line {
    position: absolute;
    left: 0; right: 0;
    text-align: center;
    line-height: 1;
    white-space: nowrap;
  }
  .title-les { top: 443px; font-size: 88px; }
  .title-main { top: 528px; font-size: 74px; }
  .title-de {
    top: 624px;
    font-size: 36px;
    display: flex;
    align-items: center;
    justify-content: center;
    gap: 22px;
  }
  .title-de .rule {
    display: block;
    width: 203px;
    height: 2px;
    background: var(--type-white);
  }
  .title-place { top: 660px; font-size: 90px; }
  .publisher-band {
    position: absolute;
    left: 0; right: 0; bottom: 0;
    height: 68px;
    background: var(--accent-red);
    display: flex;
    align-items: center;
    justify-content: center;
    font-size: 23px;
    font-weight: 700;
  }
</style>
</head>
<body>
  <div class="cover">
    <div class="cover-photo" role="img" aria-label="Photographie de Lorient au crépuscule : silhouettes de bâtiments et de lampadaires allumés sous un ciel rouge"></div>
    <div class="author">Corinne Valmer</div>
    <h1 class="title">
      <span class="title-line title-les">LES</span>
      <span class="title-line title-main">MURMURES</span>
      <span class="title-line title-de"><span class="rule"></span>DE<span class="rule"></span></span>
      <span class="title-line title-place">LORIENT</span>
    </h1>
    <div class="publisher-band">Editions Pluvane</div>
  </div>
</body>
</html>
```